Below Par Parenting

I would like a poster (size to be agreed) created for the wording that I have composed and which I have pasted below. The poster is for my own personal gratification. It is not for commercial use. The message is driven by honesty and a profound sense of mea culpa. I am open to ideas regarding style and presentation.
I am an awful parent. No question. I am not cut out for this shit. I’m too quick to temper. I turn everything into a test of wills. I’m not down for food on the floor, for having my car trashed with your stink and detritus, for having the walls of my house daubed in your greasy fingerprints. I want to listen to The Marrows not Bumble Over Dewfields on repeat. I enjoyed making you but, on reflection, I should have pulled out. Let me go back in time to that great waste of space and energy that is ante-natal classes and tell that boho with the flowery dress and curly hair, ‘Why are you concentrating on the first five seconds? All the pain comes later. Why aren’t you telling us what to do when they won’t sleep, when they won’t sit in their high chairs, when they won’t sleep on the aeroplane?’ Boy, I wish I could play it loosey-goosey like those left-leaning parents I see going ‘coo-coo’ in Brindisetti’s but I’m not built like that. I am a right-wing despot. It’s Nazi Germany back at my place. I’m not interested in your meltdowns and tantrums. You want to writhe on the floor in the car park going red in the face? Make my day. You want to go spastic because I won’t let you watch TV for five hours straight? I don’t give a shit. Read my lips. I won’t pander to it. My wife says you’re babies but all I see is little people with an agenda. I’ve got naughty steps and sin-bins all over the joint. I wish I wasn’t the tyrant, the Valdrumo and the Oko Temba I am but it is what it is. I blame my parents and they, in turn, will blame me and their parents. Understand I don’t want to infect you too much with my bad behavior but if you could stop making such a scene in public places with your screaming, your bitching and your all round refusal to play nice then maybe, just maybe, we’d have a chance and I wouldn’t be such an awful parent.

```html
<!DOCTYPE html>
<html lang="en">
<head>
<meta charset="utf-8">
<title>I am an awful parent</title>
<link rel="stylesheet" href="https://fonts.googleapis.com/css2?family=Roboto+Condensed:wght@400;700&display=swap">
<style>
  :root {
    --paper: #ffffff;
    --ink: #222222;
    --red: #e1262d;
    --purple: #7a3e97;
    --green: #5aa637;
    --pink: #f6d3e1;
    --yellow: #fbf1b8;
    --mint: #d4ecd3;
    --sky: #cfe3f3;
    --lilac: #e3d6ee;
  }
  html, body { margin: 0; padding: 0; overflow: hidden; background: var(--paper); }
  .poster {
    position: relative;
    width: 853px;
    height: 1200px;
    overflow: hidden;
    background: var(--paper);
    font-family: "Roboto Condensed", "Arial Narrow", sans-serif;
    font-weight: 700;
    color: var(--ink);
    font-size: 15px;
    line-height: 1.3;
  }
  .bubble { position: absolute; border-radius: 50%; opacity: .75; }
  .bubble--pink   { width: 170px; height: 170px; left: -60px; top: -50px; background: var(--pink); }
  .bubble--yellow { width: 150px; height: 150px; right: -40px; top: -30px; background: var(--yellow); }
  .bubble--mint   { width: 110px; height: 110px; right: 30px; top: 610px; background: var(--mint); }
  .bubble--sky    { width: 190px; height: 190px; left: -70px; bottom: -60px; background: var(--sky); }
  .bubble--lilac  { width: 160px; height: 160px; right: -50px; bottom: -50px; background: var(--lilac); }
  .bubble--pink2  { width: 70px; height: 70px; left: 20px; top: 700px; background: var(--pink); }

  .line { position: absolute; margin: 0; white-space: nowrap; }
  .red { color: var(--red); }
  .purple { color: var(--purple); }
  .green { color: var(--green); }

  .title { left: 62px; top: 28px; font-size: 32px; color: var(--red); line-height: 1.2; }
  .title small { font-size: 16px; color: var(--ink); margin-left: 10px; }

  .illustration {
    position: absolute;
    left: 266px; top: 320px;
    width: 280px; height: 560px;
    border-radius: 40px;
    background: linear-gradient(180deg, #f4e3c9 0%, #cfe6c4 55%, #f0d7a8 100%);
  }
  .block { white-space: normal; }
</style>
</head>
<body>
<main class="poster">
  <div class="bubble bubble--pink"></div>
  <div class="bubble bubble--yellow"></div>
  <div class="bubble bubble--mint"></div>
  <div class="bubble bubble--pink2"></div>
  <div class="bubble bubble--sky"></div>
  <div class="bubble bubble--lilac"></div>

  <div class="illustration" role="img" aria-label="Illustration of a screaming toddler throwing food from a high chair"></div>

  <h1 class="line title">I am an awful parent.<small>No question.</small></h1>

  <p class="line" style="left:62px; top:80px;">I am not cut out for this shit. I’m too quick to temper.</p>
  <p class="line" style="left:370px; top:104px;">I turn everything into a test of wills.</p>

  <p class="line purple" style="left:30px; top:138px; font-size:16px;">I’m not down for food on the floor, for having my car trashed with your stink and detritus,</p>
  <p class="line purple" style="left:30px; top:160px; font-size:16px;">for having the walls of my house daubed in your greasy fingerprints.</p>

  <p class="line" style="left:90px; top:188px; font-size:16px;">I want to listen to The Marrows not Bumble Over Dewfields on repeat.</p>
  <p class="line" style="left:330px; top:216px; font-size:16px;">I enjoyed making you but, on reflection, I should have pulled out.</p>

  <p class="line" style="left:40px; top:248px;">Let me go back in time to that great waste of space and energy that is ante-natal classes and tell</p>
  <p class="line" style="left:40px; top:270px;">that boho with the flowery dress and curly hair, ‘Why are you concentrating on the first five seconds?</p>
  <p class="line" style="left:40px; top:294px;">All the pain comes later.</p>

  <p class="line block red" style="left:62px; top:324px; width:190px;">Why aren’t you telling us what to do when they won’t sleep, when they won’t sit in their high chairs, when they won’t sleep on the aeroplane?’</p>

  <p class="line block" style="left:560px; top:324px; width:265px; font-size:15px; text-align:right;">Boy, I wish I could play it loosey-goosey like those left-leaning parents I see going ‘coo-coo’ in Brindisetti’s but I’m not built like that.</p>

  <p class="line red" style="left:580px; top:440px; line-height:1.35;">I’m not interested<br>in your meltdowns<br>and tantrums.</p>

  <p class="line" style="left:60px; top:470px; font-size:16px; line-height:1.4;">I am a right-wing despot.<br>It’s Nazi Germany back<br>at my place.</p>

  <p class="line" style="left:565px; top:530px; line-height:1.35;">You want to go spastic<br>because I won’t let you watch TV<br>for five hours straight?</p>

  <p class="line green" style="left:30px; top:568px; font-size:13px; line-height:1.35;">You want to writhe on the floor<br>in the car park going red in the face?</p>

  <p class="line" style="left:150px; top:622px;">Make my day.</p>

  <p class="line" style="left:255px; top:896px;">I don’t give a shit. Read my lips. I won’t pander to it.</p>

  <p class="line green" style="left:40px; top:932px;">My wife says you’re babies but all I see is little people with an agenda.</p>
  <p class="line green" style="left:40px; top:954px;">I’ve got naughty steps and sin-bins all over the joint.</p>

  <p class="line" style="left:225px; top:996px;">I wish I wasn’t the tyrant, the Valdrumo and the Oko Temba I am but it is what it is.</p>

  <p class="line" style="left:40px; top:1040px; font-size:16px;">I blame my parents and they, in turn, will blame me and their parents.</p>

  <p class="line block red" style="left:40px; top:1080px; width:775px;">Understand I don’t want to infect you too much with my bad behavior but if you could stop making such a scene in public places with your screaming, your bitching and your all round refusal to play nice then maybe, just maybe, we’d have a chance and I wouldn’t be such an awful parent.</p>
</main>
</body>
</html>
```